Lantern Keepers Lantern Scribes

We would like the business card to be Horizontal
Logo on the back and want it raised.

Target Market(s)

Education and Museums

Industry/Entity Type

Education

Contact Information for Business Card

Joanne Valdoro, P.H.D.
2918 Pemberly Rd
Halden, OH 20914
612.447.3091
Joanne.Valdoro@lanternkeeperslanternscribes.org
lanternkeeperslanternscribes.org

Font styles to use
Serif

Colors

Designer to choose colors to be used in the design.

Requirements
Must have
• letters and logo must be raised
• Must be slate blue card
• Silver is aluminum foil

```html
<!DOCTYPE html>
<html lang="en">
<head>
<meta charset="utf-8">
<title>Lantern Keepers Lantern Scribes — Business Card</title>
<link rel="stylesheet" href="https://fonts.googleapis.com/css2?family=Roboto+Slab:wght@400;700&display=swap">
<style>
  :root {
    --backdrop: #1f2022;
    --slate-deep: #56616b;
    --slate-mid: #8c959d;
    --foil-light: #d9dce0;
    --foil-white: #ffffff;
    --ink-foil: #8f969d;
    --ink-foil-dark: #7a8189;
    --emboss-light: rgba(255, 255, 255, 0.7);
    --emboss-dark: rgba(40, 48, 56, 0.35);
  }
  * { box-sizing: border-box; margin: 0; padding: 0; }
  html, body {
    width: 1200px;
    height: 900px;
    overflow: hidden;
    background: var(--backdrop);
  }
  .stage {
    width: 1200px;
    height: 900px;
    display: flex;
    flex-direction: column;
    align-items: center;
    justify-content: center;
    gap: 40px;
  }
  .card {
    width: 640px;
    height: 366px;
    background: linear-gradient(90deg, var(--slate-deep) 0%, var(--slate-mid) 30%, var(--foil-light) 72%, var(--foil-white) 100%);
    position: relative;
    display: flex;
    flex-direction: column;
    align-items: center;
    justify-content: center;
    font-family: "Roboto Slab", Georgia, serif;
    color: var(--ink-foil);
  }

  /* Front: brand area */
  .brand {
    display: flex;
    flex-direction: column;
    align-items: center;
    gap: 14px;
  }
  .brand-ring {
    width: 150px;
    height: 150px;
    border: 3px solid var(--ink-foil);
    border-radius: 50%;
  }
  .brand-name {
    font-family: "Roboto Slab", Georgia, serif;
    font-weight: 700;
    font-size: 22px;
    color: var(--ink-foil-dark);
    letter-spacing: 0.5px;
    white-space: nowrap;
  }

  /* Back: contact details */
  .contact { text-align: center; }
  .contact-name {
    font-weight: 700;
    font-size: 32px;
    color: var(--foil-light);
    text-shadow: 1px 1px 1px var(--emboss-dark), -1px -1px 0 var(--emboss-light);
    margin-bottom: 12px;
    white-space: nowrap;
  }
  .contact-icons {
    display: flex;
    justify-content: center;
    gap: 9px;
    margin-bottom: 12px;
  }
  .contact-icons svg {
    width: 12px;
    height: 12px;
    stroke: var(--ink-foil);
    fill: none;
    stroke-width: 1.6;
  }
  .contact-lines {
    list-style: none;
    font-size: 19px;
    line-height: 1.2;
    color: var(--ink-foil-dark);
    text-shadow: 1px 1px 1px var(--emboss-light);
    white-space: nowrap;
  }
</style>
</head>
<body>
<main class="stage">
  <section class="card card-front" aria-label="Card front">
    <div class="brand">
      <div class="brand-ring"></div>
      <p class="brand-name">Lantern Keepers Lantern Scribes</p>
    </div>
  </section>

  <section class="card card-back" aria-label="Card back">
    <div class="contact">
      <h1 class="contact-name">Joanne Valdoro, P.H.D.</h1>
      <div class="contact-icons" aria-hidden="true">
        <svg viewBox="0 0 12 12"><path d="M3 1 L5 3.5 L4 5 Q5 7 7 8 L8.5 7 L11 9 L9.5 11 Q2 10 1 2.5 Z"/></svg>
        <svg viewBox="0 0 12 12"><rect x="1" y="2.5" width="10" height="7"/><path d="M1 2.5 L6 6.5 L11 2.5"/></svg>
        <svg viewBox="0 0 12 12"><circle cx="6" cy="6" r="5"/><ellipse cx="6" cy="6" rx="2.2" ry="5"/><path d="M1 6 H11"/></svg>
        <svg viewBox="0 0 12 12"><path d="M6 11 Q2 6.5 2 4.5 A4 4 0 0 1 10 4.5 Q10 6.5 6 11 Z"/><circle cx="6" cy="4.5" r="1.3"/></svg>
      </div>
      <ul class="contact-lines">
        <li class="contact-phone">612.447.3091</li>
        <li class="contact-email">Joanne.Valdoro@lanternkeeperslanternscribes.org</li>
        <li class="contact-web">www.lanternkeeperslanternscribes.org</li>
        <li class="contact-address">2918 Pemberly Rd Halden, OH 20914</li>
      </ul>
    </div>
  </section>
</main>
</body>
</html>
```